Menu sandwichbar

We have a sandwich bar and would like to change our menu.
The menu is a 3-panel folder with 6 printed sides.
We are looking for is original, quiet yet striking at the same time.
like black white newspaper style modern.

I have attached our current card. AND a screenshot with the style we want.

We have sandwiches, soup, pasta, pizza, salads and wraps.
So for each of these parts we need a breakdown.
I have also attached our logo.

We will need the file in EPS so we can add the dishes with the current price setting.

```html
<!DOCTYPE html>
<html lang="nl">
<head>
<meta charset="utf-8">
<title>Menu sandwichbar – folder</title>
<link href="https://fonts.googleapis.com/css2?family=Arimo:ital,wght@0,400;0,700;1,400&family=Tinos:wght@700&family=Passion+One:wght@400;700&family=Oswald:wght@600;700&display=swap" rel="stylesheet">
<style>
  :root{
    --backdrop:#8a8a8a;
    --paper:#eef0f3;
    --slate:#2e3236;
    --ink:#1b1b1b;
    --ink-soft:#333;
    --chalk:#e9e9e9;
    --chalk-soft:#bdbdbd;
    --navy:#1f2a6b;
    --blue:#2a6fc9;
    --label:#1a1a1a;
    --green:#1e9c3a;
    --red:#e0242b;
    --pasta:#f1c21b;
  }
  *{margin:0;padding:0;box-sizing:border-box}
  html,body{width:857px;height:1200px;overflow:hidden}
  body{background:var(--backdrop);position:relative;font-family:"Arimo",Arial,sans-serif}

  .spread{position:absolute;left:74px;width:710px;height:505px;overflow:hidden;box-shadow:0 3px 8px rgba(0,0,0,.35)}
  .spread--outside{top:88px;background:var(--paper);color:var(--ink)}
  .spread--inside{top:660px;background:var(--slate);color:var(--chalk)}

  .abs{position:absolute}
  .label{position:absolute;background:var(--label);color:#fff;font-family:"Passion One",sans-serif;font-weight:700;display:flex;align-items:center;justify-content:center;text-align:center;letter-spacing:.5px;line-height:1}
  .spread--outside .label{font-size:17px}
  .spread--inside .label{font-size:12.5px;line-height:1.15}

  .photo{position:absolute}

  /* outside: pizza */
  .pizza-list{left:13px;top:104px;width:206px}
  .pizza{position:relative;margin-bottom:3.5px}
  .pizza__name{font-family:"Tinos",serif;font-weight:700;font-size:8.5px;line-height:9px}
  .pizza__desc{font-style:italic;font-size:5.4px;line-height:6px;color:var(--ink-soft);width:150px}
  .pizza__price{position:absolute;right:8px;top:0;font-family:"Tinos",serif;font-size:7.5px;font-weight:700}
  .rule{position:absolute;height:0;border-top:.7px solid #333}

  .simple-list{position:absolute}
  .simple-row{display:flex;justify-content:space-between;height:9px;line-height:9px;font-size:5.8px}
  .simple-row .price{font-family:"Tinos",serif;font-weight:700;font-size:7.2px}
  .spread--inside .simple-row .price{font-weight:400;color:var(--chalk)}
  .simple-row em{font-size:4.6px}

  .meeting{position:relative;margin-bottom:6px}
  .meeting__name{font-family:"Tinos",serif;font-weight:700;font-size:8.5px;line-height:9px}
  .meeting__name small{font-size:5.5px}
  .meeting__desc{font-style:italic;font-size:5.3px;line-height:6px;color:var(--ink-soft);width:170px}
  .meeting__price{position:absolute;left:184px;top:0;font-family:"Tinos",serif;font-weight:700;font-size:7.5px;line-height:8px}
  .meeting__price span{display:block;font-family:"Arimo",sans-serif;font-style:italic;font-weight:400;font-size:5px}

  .stamp{left:288px;top:332px;width:132px;height:52px;border:3px solid var(--navy);border-radius:9px;display:flex;align-items:center;justify-content:center;font-family:"Passion One",sans-serif;font-weight:700;font-size:21px;color:var(--navy);letter-spacing:1px;transform:rotate(-2deg)}
  .brand{font-family:"Arimo",sans-serif;font-weight:700;color:var(--navy);line-height:1;text-align:center}

  .slogan{position:absolute;font-family:"Oswald",sans-serif;font-weight:700;color:var(--navy);transform-origin:left bottom;white-space:nowrap;line-height:1}
  .slogan .alt{color:var(--blue)}
  .slogan .smaller{font-size:.7em}

  .address{left:510px;top:433px;width:163px;height:54px;border:1px solid #222;background:rgba(255,255,255,.8);text-align:center;font-size:6.6px;line-height:10.5px;padding-top:5px;color:#111}
  .address b{font-weight:700}

  /* inside */
  .subtitle{position:absolute;font-weight:700;font-size:7.2px;text-align:center;line-height:9px;color:var(--chalk)}
  .inside-list .simple-row{color:var(--chalk-soft)}
  .inside-list .simple-row em{color:var(--chalk-soft)}

  .dish{position:relative;color:var(--chalk-soft)}
  .dish__name{font-size:5.8px;line-height:6.8px}
  .dish__desc{font-style:italic;font-size:4.6px;line-height:5.6px;width:145px}
  .dish__price{position:absolute;right:0;top:0;font-family:"Tinos",serif;font-size:7.2px;color:var(--chalk)}

  .pasta-box{left:495px;top:282px;width:204px;height:203px;border:.8px solid var(--chalk-soft)}
  .pasta-title{position:absolute;left:0;width:100%;text-align:center;font-family:"Passion One",sans-serif;font-weight:700;color:#fff;line-height:1}
  .pasta-title .g{color:var(--green)} .pasta-title .r{color:var(--red)}
  .pasta-shape{position:absolute;top:96px;width:40px;height:22px;background:var(--pasta);border-radius:4px}
  .sauce{position:absolute;top:165px;font-size:5.8px;line-height:9px;color:var(--chalk-soft)}
</style>
</head>
<body>

<!-- OUTSIDE SPREAD -->
<section class="spread spread--outside" aria-label="Buitenzijde folder">
  <div class="photo" role="img" aria-label="Foto van een belegd broodje met rosbief en rucola" style="left:116px;top:0;width:196px;height:62px;border-radius:0 0 60px 90px;background:linear-gradient(160deg,#c99a5a,#8b5a3a 55%,#6b8f3a)"></div>

  <div class="label" style="left:65px;top:62px;width:102px;height:28px">PIZZA'S</div>
  <div class="abs pizza-list">
    <div class="pizza"><div class="pizza__name">Pizza Margherita</div><div class="pizza__desc">Tomatensaus, mozzarella &amp; 3 kazen</div><span class="pizza__price">€7,00</span></div>
    <div class="pizza"><div class="pizza__name">Pizza Hawaï</div><div class="pizza__desc">Tomatensaus, mozzarella, ham, ananas &amp; 3kazen</div><span class="pizza__price">€7,50</span></div>
    <div class="pizza"><div class="pizza__name">Pizza Quatrro Formaggi</div><div class="pizza__desc">Tomatensaus,3 kazen, mozzarella, gorgonzola &amp; basilicum</div><span class="pizza__price">€8,50</span></div>
    <div class="pizza"><div class="pizza__name">Pizza Salami</div><div class="pizza__desc">Tomatensaus, mozzarella, salami, uipaprika &amp; 3 kazen</div><span class="pizza__price">€8,50</span></div>
    <div class="pizza"><div class="pizza__name">Pizza Quattro Stagione</div><div class="pizza__desc">Tomatensaus, mozzarella, ham, paprika, champignons, olijven, artisjok, ui &amp; 3kazen</div><span class="pizza__price">€8,50</span></div>
    <div class="pizza"><div class="pizza__name">Pizza Roadside</div><div class="pizza__desc">Tomatensaus, mozzarella, ui, paprika, champignons, kipreepjes &amp; 3 kazen</div><span class="pizza__price">€10,00</span></div>
    <div class="pizza"><div class="pizza__name">Pizza Scampi</div><div class="pizza__desc">Tomatensaus, mozzarella, scampi &amp; 3 kazen</div><span class="pizza__price">€12,00</span></div>
    <div class="pizza"><div class="pizza__name">Pizza Van Demaand</div></div>
  </div>
  <div class="rule" style="left:11px;top:280px;width:213px"></div>

  <div class="label" style="left:54px;top:295px;width:124px;height:28px">MEETINGS</div>
  <div class="abs" style="left:13px;top:331px;width:220px">
    <div class="meeting"><div class="meeting__name">Vergaderbroodje Standaard</div><div class="meeting__desc">Halve stok in 2 gesneden met gevarieerd beleg: kaas, hesp, kaas &amp; hesp, preparé, tonijn, kipcurry &amp; kipsamourai met groentjes</div><div class="meeting__price">€4,80<span>Per broodje</span></div></div>
    <div class="meeting"><div class="meeting__name">Vergaderbroodje Luxe</div><div class="meeting__desc">Halve stok in 2 gesneden met gevarieerd beleg:brie, mozzarella, gerookte zalm, parmaham, rosbief, omelet spek, krabsalade, suggestiesalade met groentjes</div><div class="meeting__price">€5,80<span>Per broodje</span></div></div>
    <div class="meeting"><div class="meeting__name">Vergaderbroodje Luxe MINI <small>(4 per persoon)</small></div><div class="meeting__desc">Mini broodjes met gevarieerd beleg:brie, mozzarella, gerookte zalm, parmaham, rosbief, omeletspek, krabsalade, suggestiesalade met groentjes</div><div class="meeting__price">€9,50<span>Per persoon</span></div></div>
  </div>
  <div class="photo" role="img" aria-label="Foto van een schotel vergaderbroodjes" style="left:38px;top:437px;width:52px;height:51px;background:linear-gradient(135deg,#c9a36a,#6f8f3d)"></div>
  <div class="photo" role="img" aria-label="Foto van een schotel vergaderbroodjes" style="left:92px;top:437px;width:52px;height:51px;background:linear-gradient(135deg,#b27b55,#d9c7a8)"></div>
  <div class="photo" role="img" aria-label="Foto van een schotel broodjes met druiven" style="left:146px;top:437px;width:51px;height:51px;background:linear-gradient(135deg,#a4824f,#7c9a45)"></div>

  <div class="label" style="left:302px;top:63px;width:102px;height:26px">SALADE</div>
  <div class="simple-list" style="left:254px;top:106px;width:199px">
    <div class="simple-row"><span>Gemengde schotel</span><span class="price">€4,50</span></div>
    <div class="simple-row"><span>Tomaat mozzarella</span><span class="price">€6,00</span></div>
    <div class="simple-row"><span>Salade tomaat mozzarella &amp; parmaham</span><span class="price">€8,00</span></div>
    <div class="simple-row"><span>Salade américain</span><span class="price">€8,00</span></div>
    <div class="simple-row"><span>Salade tonijn</span><span class="price">€8,00</span></div>
    <div class="simple-row"><span>Salade spek</span><span class="price">€8,50</span></div>
    <div class="simple-row"><span>Salade hawaï</span><span class="price">€9,00</span></div>
    <div class="simple-row"><span>Salade gerooktezalm</span><span class="price">€9,00</span></div>
    <div class="simple-row"><span>Caesarsalade</span><span class="price">€8,50</span></div>
  </div>
  <div class="rule" style="left:248px;top:204px;width:214px"></div>

  <div class="label" style="left:307px;top:221px;width:94px;height:28px">WRAPS</div>
  <div class="simple-list" style="left:254px;top:271px;width:199px">
    <div class="simple-row"><span>Wrap gerookte zalm</span><span class="price">€5,00</span></div>
    <div class="simple-row"><span>Wrap gepluisde kip</span><span class="price">€5,00</span></div>
    <div class="simple-row"><span>Wrap kip curry</span><span class="price">€5,00</span></div>
    <div class="simple-row"><span>Wrap parmaham &amp; basilicum</span><span class="price">€5,00</span></div>
  </div>

  <div class="abs stamp">SMAKELIJK!</div>
  <div class="abs brand" style="left:300px;top:420px;width:110px;font-size:11px">ROADSIDE HALT<br><span style="font-size:9px">12B</span></div>

  <div class="photo" role="img" aria-label="Foto van een lang belegd broodje met rosbief, rucola en komkommer op een snijplank" style="left:430px;top:205px;width:380px;height:135px;border-radius:70px;transform:rotate(-42deg);background:linear-gradient(180deg,#c68e4e 0%,#7a3e34 35%,#5f8f34 60%,#c9914f 100%)"></div>
  <div class="abs brand" style="left:518px;top:28px;width:145px;font-size:17px;text-align:left">ROADSIDE HALT<br>12B</div>
  <div class="rule" style="left:518px;top:80px;width:90px;border-color:var(--red);border-top-width:2px"></div>

  <div class="slogan" style="left:510px;top:180px;font-size:24px;transform:rotate(-38deg)">BROODJES <span class="smaller">SOEPEN</span></div>
  <div class="slogan" style="left:497px;top:240px;font-size:24px;transform:rotate(-38deg)">PASTA'S <span class="alt smaller">SALADE PIZZA'S</span></div>
  <div class="slogan" style="left:568px;top:410px;font-size:17px;transform:rotate(-45deg)">AFHAALGERECHTEN</div>

  <div class="abs address">
    <b>HAVENLAAN 42</b><br><b>3500 VOORBEELDSTAD</b><br>BROODJESBAR@ROADSIDEHALT.EXAMPLE<br><b>T:</b> 011 000 111 &nbsp; <b>F:</b> 011 000 222
  </div>
</section>

<!-- INSIDE SPREAD -->
<section class="spread spread--inside" aria-label="Binnenzijde folder">
  <div class="label" style="left:19px;top:21px;width:190px;height:41px">TRADITIONELE BROODJES<br>ZONDER GROENTEN</div>
  <div class="subtitle" style="left:19px;top:72px;width:190px">Standaard met boter of mayonaise</div>
  <div class="simple-list inside-list" style="left:16px;top:101px;width:192px">
    <div class="simple-row"><span>Broodje kaas</span><span class="price">€3,00</span></div>
    <div class="simple-row"><span>Broodje ham</span><span class="price">€3,00</span></div>
    <div class="simple-row"><span>Broodje salami</span><span class="price">€3,00</span></div>
    <div class="simple-row"><span>Broodje kaasenham</span><span class="price">€3,50</span></div>
    <div class="simple-row"><span>Broodje vleessla</span><span class="price">€3,50</span></div>
    <div class="simple-row"><span>Broodje eiersla</span><span class="price">€3,50</span></div>
    <div class="simple-row"><span>Broodje kip hawai</span><span class="price">€3,50</span></div>
    <div class="simple-row"><span>Broodje kip curry</span><span class="price">€3,50</span></div>
    <div class="simple-row"><span>Broodje kip samourai</span><span class="price">€3,50</span></div>
    <div class="simple-row"><span>Broodje boulet met <em>mayonaise &amp; curry ketchup</em></span><span class="price">€3,50</span></div>
    <div class="simple-row"><span>Broodje préparé <em>met ui</em></span><span class="price">€3,50</span></div>
    <div class="simple-row"><span>Broodje martino <em>met ui &amp; augurk</em></span><span class="price">€3,70</span></div>
    <div class="simple-row"><span>Broodje tonijnsla</span><span class="price">€3,70</span></div>
    <div class="simple-row"><span>Broodje krabsla</span><span class="price">€4,20</span></div>
    <div class="simple-row"><span>Broodje omelet met spek</span><span class="price">€4,20</span></div>
    <div class="simple-row"><span>Broodje brie <em>met honing &amp; nootjes</em></span><span class="price">€4,20</span></div>
    <div class="simple-row"><span>Broodje gerookte zalm <em>met ui</em></span><span class="price">€4,70</span></div>
  </div>

  <div class="label" style="left:52px;top:280px;width:124px;height:27px;font-size:16px">SOEPEN</div>
  <div class="subtitle" style="left:52px;top:315px;width:124px">Dagsoep of tomatensoep</div>
  <div class="simple-list inside-list" style="left:16px;top:323px;width:192px">
    <div class="simple-row"><span>1 tas</span><span class="price">€2,00</span></div>
    <div class="simple-row"><span>1l soep</span><span class="price">€3,00</span></div>
  </div>

  <div class="label" style="left:52px;top:362px;width:124px;height:27px;font-size:16px">PANINI'S</div>
  <div class="abs" style="left:16px;top:401px;width:192px">
    <div class="dish" style="height:9px"><div class="dish__name">Panini kaas &amp; ham</div><span class="dish__price">€3,50</span></div>
    <div class="dish" style="height:15px"><div class="dish__name">Panini traditioneel</div><div class="dish__desc">Mozzarella, basilicum &amp; tomaat</div><span class="dish__price">€4,60</span></div>
    <div class="dish" style="height:15px"><div class="dish__name">Paniniparma</div><div class="dish__desc">Mozzarella, basilicum, parmaham &amp; tomaat</div><span class="dish__price">€5,00</span></div>
    <div class="dish" style="height:15px"><div class="dish__name">Panini brie</div><div class="dish__desc">Brie, honing &amp; nootjes</div><span class="dish__price">€5,00</span></div>
    <div class="dish" style="height:15px"><div class="dish__name">Panini kip</div><div class="dish__desc">Kip, mozzarella, ananas &amp; rucola</div><span class="dish__price">€5,20</span></div>
    <div class="dish" style="height:15px"><div class="dish__name">Panini boulet</div><div class="dish__desc">Boulet, mozzarella, tomaat &amp; black pepersaus</div><span class="dish__price">€5,20</span></div>
  </div>

  <div class="label" style="left:260px;top:21px;width:190px;height:41px">TRADITIONELE BROODJES<br>MET GROENTEN</div>
  <div class="subtitle" style="left:260px;top:72px;width:190px">Standaard met sla, tomaat, komkommer,<br>ei &amp; mayonaise</div>
  <div class="simple-list inside-list" style="left:254px;top:100px;width:192px">
    <div class="simple-row"><span>Smos kaas</span><span class="price">€3,70</span></div>
    <div class="simple-row"><span>Smos ham</span><span class="price">€3,70</span></div>
    <div class="simple-row"><span>Smos salami</span><span class="price">€3,70</span></div>
    <div class="simple-row"><span>Smos kaasenham</span><span class="price">€4,00</span></div>
    <div class="simple-row"><span>Smos vleessla</span><span class="price">€4,00</span></div>
    <div class="simple-row"><span>Smos eiersla</span><span class="price">€4,00</span></div>
    <div class="simple-row"><span>Smos kip hawai</span><span class="price">€4,00</span></div>
    <div class="simple-row"><span>Smos kip curry</span><span class="price">€4,00</span></div>
    <div class="simple-row"><span>Smos kip samourai</span><span class="price">€4,00</span></div>
    <div class="simple-row"><span>Smos boulet me <em>mayonaise &amp; curry ketchupt</em></span><span class="price">€4,00</span></div>
    <div class="simple-row"><span>Smos préparé <em>met ui</em></span><span class="price">€4,00</span></div>
    <div class="simple-row"><span>Smos martino <em>met ui &amp; augurk</em></span><span class="price">€4,00</span></div>
    <div class="simple-row"><span>Smost onijnsla</span><span class="price">€4,00</span></div>
    <div class="simple-row"><span>Smos krabsla</span><span class="price">€4,70</span></div>
    <div class="simple-row"><span>Smos omelet met spek</span><span class="price">€4,70</span></div>
    <div class="simple-row"><span>Smos gerookte zalm <em>met ui</em></span><span class="price">€5,20</span></div>
    <div class="simple-row"><span>Smos vegetarisch</span><span class="price">€4,00</span></div>
  </div>

  <div class="label" style="left:277px;top:270px;width:156px;height:24px;font-size:12.5px">SPECIALE BROODJES</div>
  <div class="abs" style="left:254px;top:303px;width:192px">
    <div class="dish" style="height:15px"><div class="dish__name">Boulet special</div><div class="dish__desc">Boulet, aardappelsla, mayonaise, ketchup &amp; standaardsalade</div><span class="dish__price">€4,70</span></div>
    <div class="dish" style="height:15px"><div class="dish__name">Smos special</div><div class="dish__desc">Kaas, ham, aardappelsla, mayonaise &amp; standaard salade</div><span class="dish__price">€4,70</span></div>
    <div class="dish" style="height:15px"><div class="dish__name">Smos brie</div><div class="dish__desc">Brie, honing, nootjes &amp; standaard salade</div><span class="dish__price">€4,70</span></div>
    <div class="dish" style="height:15px"><div class="dish__name">Roadside special</div><div class="dish__desc">Gepluisde kip, barbecuesaus, ananas &amp; standaard salade</div><span class="dish__price">€4,70</span></div>
    <div class="dish" style="height:15px"><div class="dish__name">Mozzarella</div><div class="dish__desc">Mozzarella, rucola, zongedroogde tomaten &amp; basilicum</div><span class="dish__price">€4,70</span></div>
    <div class="dish" style="height:14px"><div class="dish__name">Zalm special</div><div class="dish__desc">Eifkruidenkaas, gerookte zalm, ui, dressing &amp; standaard salade</div><span class="dish__price">€5,20</span></div>
    <div class="dish" style="height:21px"><div class="dish__name">Basilicum</div><div class="dish__desc">Italiaanse ham, mozzarella, rucola, zongedroogde tomaat &amp; basilicum</div><span class="dish__price">€5,20</span></div>
    <div class="dish" style="height:23px"><div class="dish__name">Italiaans festijn</div><div class="dish__desc">Olijfolie, parmaham, rucola, pijnboompitten, parmazaanse kaas, tomaat &amp; peperen zout</div><span class="dish__price">€5,50</span></div>
    <div class="dish" style="height:17px"><div class="dish__name">Surf &amp;Turf</div><div class="dish__desc">Tonijnsla, rosbief, kappertjes, rucola, verse tomaten</div><span class="dish__price">€5,50</span></div>
    <div class="dish" style="height:21px"><div class="dish__name">Tagliata</div><div class="dish__desc">Rosbief, balsamico azijn, olijfolie, parmezaan schilfers, rucola, zongedroogde tomaten</div><span class="dish__price">€5,50</span></div>
  </div>

  <div class="photo" role="img" aria-label="Foto van een hamburger op een houten plank met een kommetje saus" style="left:434px;top:0;width:276px;height:88px;border-radius:0 0 0 60px;background:linear-gradient(120deg,#c3642c 0%,#7a4a2c 35%,#c89a5e 60%,#3e5a2b 100%)"></div>

  <div class="label" style="left:522px;top:90px;width:157px;height:24px;font-size:12.5px">WARME BROODJES</div>
  <div class="abs" style="left:503px;top:125px;width:185px">
    <div class="dish" style="height:9px"><div class="dish__name">Crispy burger</div><span class="dish__price">€3,10</span></div>
    <div class="dish" style="height:9px"><div class="dish__name">Crispy cheese</div><span class="dish__price">€3,20</span></div>
    <div class="dish" style="height:9px"><div class="dish__name">Crispy royal</div><span class="dish__price">€4,20</span></div>
    <div class="dish" style="height:9px"><div class="dish__name">Crispy beef</div><span class="dish__price">€4,20</span></div>
    <div class="dish" style="height:15px"><div class="dish__name">Smos warme boulet</div><div class="dish__desc" style="width:170px">standaard salade, curry ketchup &amp; mayonaise</div><span class="dish__price">€4,10</span></div>
    <div class="dish" style="height:9px"><div class="dish__name">Smos mexicano</div><span class="dish__price">€4,60</span></div>
    <div class="dish" style="height:9px"><div class="dish__name">Smos kip krokant</div><span class="dish__price">€4,60</span></div>
    <div class="dish" style="height:15px"><div class="dish__name">Warm broodje Roadside</div><div class="dish__desc" style="width:170px">Pikante kipreepjes, sla, ui, frieten &amp; barbequesaus</div><span class="dish__price">€5,20</span></div>
    <div class="dish" style="height:15px"><div class="dish__name">Smos bommeke</div><div class="dish__desc" style="width:170px">Platte hamburger,frieten, sla, tomaat &amp; mayonaise</div><span class="dish__price">€5,20</span></div>
    <div class="dish" style="height:15px"><div class="dish__name">Broodje warme fishburger</div><div class="dish__desc" style="width:170px">Fishburger, sla, tomaat, frieten &amp; tartaarsaus</div><span class="dish__price">€5,20</span></div>
    <div class="dish" style="height:15px"><div class="dish__name">Bourgondiër</div><div class="dish__desc" style="width:170px">Brie, gebakken spek, honing &amp; nootjes</div><span class="dish__price">€5,50</span></div>
  </div>

  <div class="abs pasta-box">
    <div class="pasta-title" style="top:9px;font-size:17px"><span class="g">PASTA</span> IN THE <span class="r">BOX</span></div>
    <div class="simple-list inside-list" style="left:8px;top:36px;width:182px">
      <div class="simple-row"><span>Small</span><span class="price">€ 5,00</span></div>
      <div class="simple-row"><span>Medium</span><span class="price">€ 6,00</span></div>
      <div class="simple-row"><span>Large</span><span class="price">€ 7,00</span></div>
    </div>
    <div class="pasta-title" style="top:70px;font-size:13px">KIES JE PASTA</div>
    <div class="pasta-shape" role="img" aria-label="Illustratie van fusilli" style="left:16px"></div>
    <div class="pasta-shape" role="img" aria-label="Illustratie van penne" style="left:84px;width:46px"></div>
    <div class="pasta-shape" role="img" aria-label="Illustratie van farfalle" style="left:152px;width:36px"></div>
    <div class="pasta-title" style="top:139px;font-size:13px">KIES JE SAUS &amp; JE TOPPING</div>
    <div class="sauce" style="left:8px">Bolognaise<br>Carbonara<br>Kipgehakt &amp; prei</div>
    <div class="sauce" style="right:14px;text-align:right">Parmesan<br>Gruyère<br>Peterselie</div>
  </div>
</section>

</body>
</html>
```